Professional, Attractive, Simple Website Needed!!

We completed the design for our logo.

We need a website built out around this.

Here are a couple samples of how we want ours formatted.

http://brvntapower.com

http://www.halvorbeam.com/lp/free-quote?LeadSource=Search%20Engine&ProgramName=webquery&experience=qual&language=en&type=brd&gclid=Xq7RTPwmEYKDLAvUHbsNQkfPZrTcGwnJuoVbXeLqHmRYdAsWtPkMcNfBYgzTrUoQJhEdWvKpYaLsZbCmNDgQwTxAoKpXbT_qkR

http://morvalo.co

Reason: Extending this deadline due to our delay in providing designers with content for each page. This is coming in next 24 hours.

Reason: Due to scheduling conflicts and extended travel delays related to Puerto Rico, the deadline has been extended. Your patience is greatly appreciated.

Reason: Travel and scheduling conflicts have made it impossible to give this project the thorough review it deserves, therefore I am extending the deadline. Thank you for your patience!

Target Market(s)

Home Owners who earn 60k + household annually

Industry/Entity Type

It Professional

Coding

Coded - Design and coding required

Number of Pages Required

5+ page

Font styles to use
Serif

Colors
34a7d8
9bcb3c

Requirements
Must have
• Simple
• Lead form Entry (Ability for visitor to enter Name, number and address for a quote)
• Sleek Design
• Professional
• Testimonials
• Use color Scheme of Design Logo Attached
Nice to have
• Video when site starts
• Like this
• https://www.vidmarrow.com/watch?v=qT8mRpXw2Ka&feature=vidm.ro
Should not have
• Should not include Commercial solar
• Should not include wind power

```html
<!DOCTYPE html>
<html lang="en">
<head>
<meta charset="utf-8">
<title>Brightvale Energy</title>
<link href="https://fonts.googleapis.com/css2?family=Roboto:wght@300;400;700&family=Roboto+Condensed:wght@700&display=swap" rel="stylesheet">
<style>
  :root{
    --navy:#262c3a;
    --ink:#2b2f36;
    --muted:#5d6470;
    --green:#9bcb3c;
    --blue:#1e8ccc;
    --white:#ffffff;
  }
  *{margin:0;padding:0;box-sizing:border-box}
  html,body{width:1200px;height:1200px;overflow:hidden;background:var(--white);font-family:'Roboto',sans-serif}
  .page{position:relative;width:1200px;height:1200px}

  .video-frame{position:absolute;left:234px;top:0;width:731px;height:37px;background:#1d1f24;box-shadow:0 10px 24px rgba(0,0,0,.18)}
  .video-controls{position:absolute;left:80px;top:0;width:569px;height:26px;background:linear-gradient(90deg,#3a3d44,#55504d 70%,#3a3d44);display:flex;align-items:center;gap:10px;padding:0 14px;color:#ddd;font-size:8px}
  .video-progress{position:absolute;left:0;top:2px;width:100%;height:2px;background:rgba(255,255,255,.25)}
  .video-progress span{display:block;width:34px;height:100%;background:#e62117}
  .video-controls .right{margin-left:auto;display:flex;gap:10px}

  .call-band{position:absolute;left:0;top:98px;width:1200px;height:121px;background:var(--navy);display:flex;align-items:center;justify-content:center;gap:13px}
  .call-lead{font-family:'Roboto Condensed',sans-serif;font-weight:700;font-size:12px;color:var(--white);letter-spacing:.1px;margin-top:4px}
  .call-number{font-size:46px;color:var(--green);font-weight:300;line-height:1}
  .call-number b{font-weight:700}

  .section-title{position:absolute;left:0;width:1200px;text-align:center;font-weight:300;color:var(--ink)}
  .why-title{top:282px;font-size:29px}
  .rule{position:absolute;left:573px;width:53px;height:3px;background:var(--blue)}

  .why-photo{position:absolute;left:158px;top:373px;width:429px;height:282px;background:linear-gradient(180deg,#9aa3a8 0%,#c5c9cb 30%,#3d4a5e 55%,#1d2536 100%);box-shadow:0 12px 24px rgba(0,0,0,.18)}

  .features{position:absolute;left:640px;top:369px;width:340px}
  .feature{position:relative;height:76px;padding-left:54px}
  .feature svg{position:absolute;left:0;top:3px}
  .feature h3{font-weight:400;font-size:16px;color:var(--ink);line-height:20px}
  .feature p{font-size:11.5px;line-height:17px;color:var(--muted);margin-top:4px}

  .news{position:absolute;left:0;top:716px;width:1200px;height:484px;background:var(--navy)}
  .news-title{top:54px;color:var(--white);font-weight:400;font-size:27px}
  .card{position:absolute;top:134px;width:279px}
  .card-photo{height:180px}
  .card h4{margin-top:27px;font-weight:300;font-size:19.5px;color:var(--white)}
  .card p{margin-top:16px;font-size:11px;line-height:16.6px;color:#c9ccd2;text-align:justify;font-weight:300}
  .card p em{font-style:normal;color:var(--green)}
</style>
</head>
<body>
<div class="page">

  <div class="video-frame">
    <div class="video-controls">
      <div class="video-progress"><span></span></div>
      <span>&#10074;&#10074;</span><span>&#9654;|</span><span>&#128264;</span><span>0:04 / 1:08</span>
      <div class="right"><span>CC</span><span>&#9881;</span><span>&#8690;</span></div>
    </div>
  </div>

  <div class="call-band">
    <span class="call-lead">IF YOU PREFER TO SPEAK WITH A SALES REPRESENTATIVE,</span>
    <span class="call-number">CALL <b>(888) 555-0147</b></span>
  </div>

  <h2 class="section-title why-title">WHY WE BRIGHTVALE ENERGY?</h2>
  <div class="rule" style="top:331px"></div>

  <div class="why-photo" role="img" aria-label="Installer in orange shirt working on rooftop solar panels under a cloudy sky"></div>

  <div class="features">
    <div class="feature">
      <svg width="24" height="24" viewBox="0 0 24 24" fill="none" stroke="var(--blue)" stroke-width="1.5"><path d="M3 1h13v10M3 1v21h11"/><path d="M6 6h7M6 10h5M6 14h4"/><circle cx="16" cy="16" r="4"/><path d="M19 19l4 4"/></svg>
      <h3>Heading 01</h3>
      <p>Sed id rutrum risus, ac tempus mi. Praesent pretium volutpat tortor, vitae finibus ex viverra at.</p>
    </div>
    <div class="feature">
      <svg width="24" height="24" viewBox="0 0 24 24" fill="none" stroke="var(--blue)" stroke-width="1.5"><rect x="1" y="6" width="22" height="15"/><path d="M8 6V3h8v3M1 12h22M10 11h4v3h-4z"/></svg>
      <h3>Heading 02</h3>
      <p>Sed id rutrum risus, ac tempus mi. Praesent pretium volutpat tortor, vitae finibus ex viverra at.</p>
    </div>
    <div class="feature">
      <svg width="24" height="24" viewBox="0 0 24 24" fill="none" stroke="var(--blue)" stroke-width="2.2" stroke-linecap="round" stroke-dasharray="0.1 4.2"><circle cx="12" cy="12" r="9"/></svg>
      <h3>Heading 03</h3>
      <p>Sed id rutrum risus, ac tempus mi. Praesent pretium volutpat tortor, vitae finibus ex viverra at.</p>
    </div>
    <div class="feature">
      <svg width="24" height="24" viewBox="0 0 24 24" fill="none" stroke="var(--blue)" stroke-width="1.5"><rect x="1" y="4" width="22" height="19"/><path d="M1 9h22" stroke-width="4"/><path d="M6 1v5M18 1v5"/></svg>
      <h3>Heading 04</h3>
      <p>Sed id rutrum risus, ac tempus mi. Praesent pretium volutpat tortor, vitae finibus ex viverra at.</p>
    </div>
  </div>

  <section class="news">
    <h2 class="section-title news-title">Stay Up To Date</h2>
    <div class="rule" style="top:105px;left:568px;width:53px"></div>

    <article class="card" style="left:158px">
      <div class="card-photo" role="img" aria-label="Solar panel array at sunset with trees in silhouette" style="background:linear-gradient(180deg,#e8742a 0%,#b8431d 40%,#2c3a66 65%,#1f2c5a 100%)"></div>
      <h4>ALIQUAM ANTE NEQUE</h4>
      <p><em>Sed id rutrum risus, ac tempus mi. Praesent pretium volutpat tortor,</em> vitae finibus ex viverra at. Fusce sed nunc congue dolor fringilla finibus at eget urna. Aliquam nisi tellus, gravida in felis at, auctor dictum ligula. Quisque volutpat libero a ultricies iaculis.</p>
    </article>
    <article class="card" style="left:460px">
      <div class="card-photo" role="img" aria-label="Technician in a yellow hard hat checking rooftop solar panels" style="background:linear-gradient(135deg,#cfdce8 0%,#9db6d6 40%,#2f4f9a 75%,#1e3a86 100%)"></div>
      <h4>ALIQUAM ANTE NEQUE</h4>
      <p><em>Sed id rutrum risus, ac tempus mi. Praesent pretium volutpat tortor,</em> vitae finibus ex viverra at. Fusce sed nunc congue dolor fringilla finibus at eget urna. Aliquam nisi tellus, gravida in felis at, auctor dictum ligula. Quisque volutpat libero a ultricies iaculis.</p>
    </article>
    <article class="card" style="left:762px">
      <div class="card-photo" role="img" aria-label="Brick house with solar panels on its tiled roof under a blue sky" style="background:linear-gradient(160deg,#2f7fc4 0%,#6aa6d8 35%,#a8583a 60%,#7a3b26 100%)"></div>
      <h4>ALIQUAM ANTE NEQUE</h4>
      <p><em>Sed id rutrum risus, ac tempus mi. Praesent pretium volutpat tortor,</em> vitae finibus ex viverra at. Fusce sed nunc congue dolor fringilla finibus at eget urna. Aliquam nisi tellus, gravida in felis at, auctor dictum ligula. Quisque volutpat libero a ultricies iaculis.</p>
    </article>
  </section>

</div>
</body>
</html>
```